Crestwave Glow LED - E- Commerce site

We need a website designed for an LED Billboard company that sells:
1) LED Billboards (Sales & Rental)
2) LED Gas Station lights
3) Truss Systems (Sales & Rental)
4) Sound Systems (Sales & Rental)

Attached are websites that sell similar products as Crestwave Glow LED. Target market is for business, property managers and event coordinators.
This site will need to be an e-commerce site where customers can purchase the product directly from the site. What I'm looking for is a design layout to start.

Conceptual Web Designs:
http://198.51.100.47:8087/index.html
http://www.vomilux-example.com/
http://www.tonarvoxaudio-example.com/
http://www.pelmoraboard-example.com/

Attached is the logo of the company: Please note that the new spelling of the logo is "Crestwave Glow LED" using domain " CrestwaveGlowLED.com

Industry/Entity Type

Gas Station

Number of Pages Required

5+ page

Requirements
Must have
• 1) E-Commerce - Customers will need to be able to order product from the site.
• 2) Customers will also have the option to rent the product as well.
Nice to have
• I like the image of the attached website, that has a video clip loop
• http://www.pelmoraboard-example.com/

```html
<!DOCTYPE html>
<html lang="en">
<head>
<meta charset="utf-8">
<title>Crestwave Glow LED – Store</title>
<link href="https://fonts.googleapis.com/css2?family=Orbitron:wght@600;700&family=Roboto:wght@400;500;700&family=Lato:ital@1&display=swap" rel="stylesheet">
<style>
:root{
  --yellow:#f2c230;
  --orange:#e8552b;
  --green:#3aa51f;
  --ink:#222;
  --muted:#777;
  --line:#e5e5e5;
  --link:#1f7fb6;
  --soft:#f7f7f7;
  --footer:#3a3a3a;
  --footer-dark:#2e2e2e;
  --star:#f0a020;
}
*{box-sizing:border-box;margin:0;padding:0}
html,body{width:1200px;height:2442px;overflow:hidden;background:#fff}
body{position:relative;font-family:"Roboto",sans-serif;color:var(--ink)}
.abs{position:absolute}
.topbar{top:0;left:0;width:1200px;height:49px;border-bottom:1px solid var(--line);font-size:13px;color:#555}
.topbar .welcome{left:75px;top:17px}
.topbar a{color:var(--link);text-decoration:none}
.toplinks{right:75px;top:17px;display:flex;gap:24px}
.header{top:49px;left:0;width:1200px;height:94px;border-bottom:1px solid var(--line)}
.brand{left:75px;top:30px;display:flex;align-items:center;gap:12px;font-size:26px;font-weight:700;color:var(--orange)}
.brand .dot{width:30px;height:30px;border-radius:50%;background:var(--yellow)}
.cart{right:75px;top:30px;display:flex;gap:12px;align-items:center}
.cart .t{font-size:15px;color:#333}
.cart .s{font-size:13px;color:var(--orange);margin-top:3px}
.nav{top:143px;left:0;width:1200px;height:47px;border-bottom:4px solid var(--yellow)}
.nav ul{list-style:none;display:flex;position:absolute;left:75px;top:14px;font-size:15px;color:#222}
.nav li{margin-right:38px}
.search{left:1079px;top:0;width:46px;height:43px;background:var(--yellow);display:flex;align-items:center;justify-content:center}
.hero{top:190px;left:0;width:1200px;height:486px;background:linear-gradient(100deg,#1a2a22 0%,#0e1612 45%,#050806 100%)}
.hero-photo{left:0;top:0;width:1200px;height:486px;background:radial-gradient(ellipse at 35% 45%,rgba(60,150,70,.55),transparent 45%),linear-gradient(180deg,transparent 70%,rgba(20,60,30,.6))}
.hero h1{right:77px;top:100px;text-align:right;font-family:"Orbitron",sans-serif;font-weight:700;font-size:48px;line-height:52px;color:var(--yellow);letter-spacing:1px;white-space:nowrap}
.hero p{right:77px;top:233px;width:340px;text-align:right;color:#fff;font-size:15px;line-height:23px}
.btn-shop{left:973px;top:326px;width:150px;height:40px;background:var(--orange);color:#fff;font-size:14px;font-weight:500;display:flex;align-items:center;justify-content:center;gap:12px}
.dots{left:568px;top:452px;display:flex;gap:5px}
.dots span{width:11px;height:11px;border-radius:50%;border:2px solid #333;background:#fff}
.dots span.on{background:var(--yellow);border-color:var(--yellow)}
.sec-title{font-family:"Orbitron",sans-serif;font-weight:700;font-size:23px;color:#111;letter-spacing:1px}
.sec-title::after{content:"";display:block;width:62px;height:3px;background:var(--yellow);margin-top:10px}
.sec-sub{font-size:12px;color:#ccc;text-transform:uppercase}
.rule{height:1px;background:var(--line)}
.feature-photo{left:75px;top:807px;width:241px;height:424px;background:linear-gradient(180deg,#d8dde4 0%,#b8c0cb 55%,#8c9a3a 72%,#7f8f30 100%)}
.card{top:807px;width:245px;height:496px;border:1px solid #e3e3e3;background:#fff}
.card .img{left:20px;top:25px;width:203px;height:150px}
.card h3{left:0;top:213px;width:100%;text-align:center;font-size:16px;font-weight:500;letter-spacing:.5px;line-height:20px}
.card .desc{left:25px;top:240px;width:193px;text-align:justify;text-align-last:center;font-size:12.5px;line-height:18px;color:#888}
.card .spec{left:16px;width:211px;height:28px;line-height:28px;font-size:12.5px;color:#666;border-top:1px solid #e6e6e6;padding-left:8px}
.card .spec.watt{top:319px}
.card .spec.size{top:347px}
.card .spec.temp{top:375px}
.card .price{left:24px;top:405px;font-size:16px;line-height:20px;font-weight:700;color:var(--green)}
.stars{color:var(--star);font-size:17px;letter-spacing:1px;line-height:20px}
.card .stars{left:22px;top:454px}
.cart-btn{width:36px;height:36px;border-radius:50%;background:var(--orange);display:flex;align-items:center;justify-content:center}
.card .cart-btn{right:16px;top:446px}
.latest{top:1367px;left:0;width:1200px;height:473px;background:var(--soft)}
.lp-img{top:124px;width:226px;height:207px}
.lp-name{top:350px;font-family:"Orbitron",sans-serif;font-weight:600;font-size:14px;line-height:18px;color:#222;letter-spacing:.5px}
.lp-stars{top:398px;color:var(--star);font-size:14px;letter-spacing:-1px}
.lp-price{top:393px;font-size:20px;color:var(--green)}
.testi-title{left:0;top:1900px;width:1200px;text-align:center;font-family:"Orbitron",sans-serif;font-weight:700;font-size:23px;letter-spacing:1px}
.quote{top:1960px;width:480px;font-family:"Lato",sans-serif;font-style:italic;font-size:14px;line-height:21px;color:#555;text-align:justify}
.avatar{top:2038px;width:60px;height:60px;border-radius:50%;background:var(--orange)}
.author{top:2045px;font-family:"Orbitron",sans-serif;font-weight:600;font-size:13px;color:var(--orange);letter-spacing:.5px}
.loc{top:2065px;font-family:"Lato",sans-serif;font-style:italic;font-size:13px;color:#555}
.footer{top:2149px;left:0;width:1200px;height:293px;background:var(--footer)}
.fcol h4{color:#fff;font-size:17px;font-weight:500;letter-spacing:.5px;margin-bottom:22px}
.fcol ul{list-style:none}
.fcol li{color:#eee;font-size:13px;height:27.6px}
.fcol li::before{content:"»";margin-right:8px}
.fcol{top:48px}
.fbottom{left:0;top:225px;width:1200px;height:68px;background:var(--footer-dark);border-top:1px solid #4a4a4a}
.copy{left:75px;top:26px;color:#eee;font-size:13px}
.social{right:75px;top:22px;display:flex;gap:8px}
.social span{width:24px;height:24px;border-radius:50%;background:#fff}
</style>
</head>
<body>

<div class="abs topbar">
  <div class="abs welcome">Welcome visitor you can <a>login</a> or <a>create an account</a></div>
  <div class="abs toplinks"><span>Home</span><span>Wish List (0)</span><span>My Account</span><span>Shopping Cart</span><span>Checkout</span></div>
</div>

<div class="abs header">
  <div class="abs brand"><span class="dot"></span>Crestwave Glow LED</div>
  <div class="abs cart">
    <svg width="30" height="24" viewBox="0 0 30 24"><path d="M2 9h26l-4 13H6z" fill="#333"/><path d="M9 9l6-7 6 7" stroke="#333" stroke-width="2" fill="none"/></svg>
    <div><div class="t">Shopping Cart</div><div class="s">0 item(s) - $0.0</div></div>
  </div>
</div>

<nav class="abs nav">
  <ul><li>All Products</li><li>New Products</li><li>Blends</li><li>Sort - By Function</li><li>Capsule - Fillers</li><li>Specials</li><li>Flavorings</li><li>Contact</li></ul>
  <div class="abs search"><svg width="18" height="18" viewBox="0 0 18 18"><circle cx="7.5" cy="7.5" r="5.5" stroke="#fff" stroke-width="2.5" fill="none"/><path d="M11.5 11.5l5 5" stroke="#fff" stroke-width="2.5"/></svg></div>
</nav>

<section class="abs hero">
  <div class="abs hero-photo" role="img" aria-label="Night view of a gas station canopy with a lit green pump and LED price sign"></div>
  <h1 class="abs">GAS STATION<br>LIGHTS</h1>
  <p class="abs">Lorem ipsum dolor sit amet, consectetur adipiscing elit, sed do eiusmod tempor incididunt ut labore et dolore magna aliqua.</p>
  <div class="abs btn-shop"><svg width="16" height="14" viewBox="0 0 30 24"><path d="M2 9h26l-4 13H6z" fill="#fff"/><path d="M9 9l6-7 6 7" stroke="#fff" stroke-width="2.5" fill="none"/></svg>SHOP NOW</div>
  <div class="abs dots"><span class="on"></span><span></span><span></span><span></span></div>
</section>

<h2 class="abs sec-title" style="left:73px;top:752px">FEATURED PRODUCTS</h2>
<div class="abs sec-sub" style="right:75px;top:763px">Shop most popular products</div>
<div class="abs rule" style="left:75px;top:789px;width:1050px"></div>

<div class="abs feature-photo" role="img" aria-label="Ceiling-mounted LED track spotlight"></div>

<div class="abs card" style="left:343px">
  <div class="abs img" role="img" aria-label="LED billboard on a pole" style="background:linear-gradient(135deg,#2a6fb8,#7bc143)"></div>
  <h3 class="abs">LED BILLBOARDS</h3>
  <div class="abs desc">Leading Light Suitable for workshop, warehouse, cold store, parking lot, food.</div>
  <div class="abs spec watt">Watt: 400 W</div>
  <div class="abs spec size">Size: 785*710*365mm</div>
  <div class="abs spec temp">Color Temperature: 6000 K</div>
  <div class="abs price">$1,199.00</div>
  <div class="abs stars">★★★★☆</div>
  <div class="abs cart-btn"><svg width="16" height="14" viewBox="0 0 30 24"><path d="M2 9h26l-4 13H6z" fill="#fff"/><path d="M9 9l6-7 6 7" stroke="#fff" stroke-width="2.5" fill="none"/></svg></div>
</div>

<div class="abs card" style="left:614px">
  <div class="abs img" role="img" aria-label="Aluminium stage truss frame" style="background:linear-gradient(180deg,#e4e4e4,#bdbdbd 70%,#222 71%,#333)"></div>
  <h3 class="abs">TRUSSES</h3>
  <div class="abs desc">Leading Light Suitable for workshop, warehouse, cold store, parking lot, food.</div>
  <div class="abs spec watt">Watt: 400 W</div>
  <div class="abs spec size">Size: 785*710*365mm</div>
  <div class="abs spec temp">Color Temperature: 6000 K</div>
  <div class="abs price">$1,199.00</div>
  <div class="abs stars">★★★★☆</div>
  <div class="abs cart-btn"><svg width="16" height="14" viewBox="0 0 30 24"><path d="M2 9h26l-4 13H6z" fill="#fff"/><path d="M9 9l6-7 6 7" stroke="#fff" stroke-width="2.5" fill="none"/></svg></div>
</div>

<div class="abs card" style="left:884px">
  <div class="abs img" role="img" aria-label="Group of white LED bulbs" style="background:radial-gradient(circle at 50% 55%,#e8e8e8,#fff 70%)"></div>
  <h3 class="abs">GAS STATION LIGHT</h3>
  <div class="abs desc">Leading Light Suitable for workshop, warehouse, cold store, parking lot, food.</div>
  <div class="abs spec watt">Watt: 400 W</div>
  <div class="abs spec size">Size: 785*710*365mm</div>
  <div class="abs spec temp">Color Temperature: 6000 K</div>
  <div class="abs price">$1,199.00</div>
  <div class="abs stars">★★★★☆</div>
  <div class="abs cart-btn"><svg width="16" height="14" viewBox="0 0 30 24"><path d="M2 9h26l-4 13H6z" fill="#fff"/><path d="M9 9l6-7 6 7" stroke="#fff" stroke-width="2.5" fill="none"/></svg></div>
</div>

<section class="abs latest">
  <h2 class="abs sec-title" style="left:75px;top:60px">LATEST PRODUCTS</h2>
  <div class="abs sec-sub" style="right:75px;top:70px">Shop most popular products</div>

  <div class="abs lp-img" role="img" aria-label="Roadside billboard under blue sky" style="left:78px;background:linear-gradient(180deg,#4d8fd6,#a9cdea 60%,#4a6a3a)"></div>
  <div class="abs lp-name" style="left:81px">GAS STATION<br>LIGHTS</div>
  <div class="abs lp-stars" style="left:81px">★★★★★</div>
  <div class="abs lp-price" style="left:239px">$12.50</div>

  <div class="abs lp-img" role="img" aria-label="Close-up of LED chip array" style="left:352px;background:radial-gradient(circle,#e9d9b0,#9aa3ab 70%)"></div>
  <div class="abs lp-name" style="left:355px">GAS STATION<br>LIGHTS</div>
  <div class="abs lp-stars" style="left:355px">★★★★★</div>
  <div class="abs lp-price" style="left:513px">$12.50</div>

  <div class="abs lp-img" role="img" aria-label="Hanging warm glowing light bulbs" style="left:624px;background:radial-gradient(circle at 50% 60%,#f7c060,#b86a10 60%,#5a2e05)"></div>
  <div class="abs lp-name" style="left:627px">GAS STATION<br>LIGHTS</div>
  <div class="abs lp-stars" style="left:627px">★★★★★</div>
  <div class="abs lp-price" style="left:784px">$12.50</div>

  <div class="abs lp-img" role="img" aria-label="Light bulb with sprout on green grass" style="left:892px;background:linear-gradient(180deg,#d9edb8,#9fcf58 60%,#5e9a1e)"></div>
  <div class="abs lp-name" style="left:895px">GAS STATION<br>LIGHTS</div>
  <div class="abs lp-stars" style="left:895px">★★★★★</div>
  <div class="abs lp-price" style="left:1053px">$12.50</div>
</section>

<h2 class="abs testi-title">WHAT OUR CUSTOMER S SAY</h2>
<p class="abs quote" style="left:90px">"Lorem ipsum dolor sit amet, consectetur adipiscing elit, sed do eiusmod tempor incididunt ut labore et dolore magna aliqua.Lorem ipsum dolor sit amet, consectetur adipiscing elit, sed do eiusmod tempor. "</p>
<div class="abs avatar" style="left:89px"></div>
<div class="abs author" style="left:164px">BY AUTHOR NAME</div>
<div class="abs loc" style="left:164px">location, city</div>

<p class="abs quote" style="left:631px">"Lorem ipsum dolor sit amet, consectetur adipiscing elit, sed do eiusmod tempor incididunt ut labore et dolore magna aliqua.Lorem ipsum dolor sit amet, consectetur adipiscing elit, sed do eiusmod tempor. "</p>
<div class="abs avatar" style="left:630px"></div>
<div class="abs author" style="left:705px">BY AUTHOR NAME</div>
<div class="abs loc" style="left:705px">location, city</div>

<footer class="abs footer">
  <div class="abs fcol" style="left:77px"><h4>INFORMATION</h4><ul><li>What is Crestwave Glow LED?</li><li>Delivery Information</li><li>Privacy Policy</li><li>Returns &amp; Terms of Use</li></ul></div>
  <div class="abs fcol" style="left:393px"><h4>CUSTOMER SERVICE</h4><ul><li>Contact</li><li>Returns</li><li>Site Map</li></ul></div>
  <div class="abs fcol" style="left:677px"><h4>EXTRAS</h4><ul><li>Brands</li><li>Gift Vouchers</li><li>Affiliates</li><li>Specials</li></ul></div>
  <div class="abs fcol" style="left:896px"><h4>ACCOUNT</h4><ul><li>Account</li><li>Order History</li><li>Wish List</li><li>Newsletter</li></ul></div>
  <div class="abs fbottom">
    <div class="abs copy">© 2016 Crestwave Glow LED, All Rights Reserved.</div>
    <div class="abs social"><span></span><span></span><span></span><span></span><span></span></div>
  </div>
</footer>

</body>
</html>
```